Poly Bag Packaging Motorcycle Cables - Veronzo Brand

Poly Bag Dimensions: 33cm(H) x 24cm(W)
We would like to design a genuine Poly Bag Packaging for motorcycle cables.
Veronzo, is one of the leading companies for manufacturing Motorcycles, located in Egypt. Our company is offering high-quality products, the best in the local market, with very competitive prices.
We have a limited time to get this project done, So we Highly appreciate receiving your designs ASAP.
Target Market(s)
Motorcycle Spare parts Buyers
Font styles to use
Colors
Designer to choose colors to be used in the design.
Look and feel
Each slider illustrates characteristics of the customer's brand and the style your logo design should communicate.

```html
<!DOCTYPE html>
<html lang="en">
<head>
<meta charset="utf-8">
<title>Veronzo Cables – Poly Bag</title>
<link href="https://fonts.googleapis.com/css2?family=Michroma&family=Oswald:wght@600&display=swap" rel="stylesheet">
<style>
  :root {
    --page: #ffffff;
    --bag-yellow: #ffed00;
    --band-black: #111111;
    --band-grey: #3a3a3a;
    --chrome-light: #f2f2f2;
    --chrome-mid: #9a9a9a;
    --chrome-dark: #3c3c3c;
    --badge-red: #d4141b;
    --badge-dark: #8e0c10;
    --badge-text: #ffffff;
    --photo-light: #f1f1f1;
    --photo-mid: #c9c9c9;
    --outline: #222222;
  }
  html, body {
    margin: 0;
    padding: 0;
    width: 1041px;
    height: 1200px;
    overflow: hidden;
    background: var(--page);
  }
  .canvas {
    position: relative;
    width: 1041px;
    height: 1200px;
  }
  .poly-bag {
    position: absolute;
    left: 150px;
    top: 50px;
    width: 785px;
    height: 1078px;
    background: var(--bag-yellow);
    border: 2px solid var(--outline);
    border-radius: 22px;
    box-sizing: border-box;
    overflow: hidden;
  }
  .hang-hole {
    position: absolute;
    left: 340px;
    top: 34px;
    width: 100px;
    height: 46px;
  }
  .brand-band {
    position: absolute;
    left: 0;
    top: 98px;
    width: 100%;
    height: 470px;
    background: radial-gradient(ellipse at 50% 40%, var(--band-grey) 0%, var(--band-black) 75%);
    display: flex;
    align-items: center;
    justify-content: center;
    gap: 22px;
  }
  .brand-mark-dot {
    width: 46px;
    height: 46px;
    border-radius: 50%;
    background: var(--chrome-light);
  }
  .brand-name {
    font-family: "Michroma", sans-serif;
    font-size: 62px;
    letter-spacing: 4px;
    color: var(--chrome-light);
    margin: 0;
  }
  .product-title {
    position: absolute;
    left: 0;
    top: 600px;
    width: 100%;
    margin: 0;
    text-align: center;
    font-family: "Michroma", sans-serif;
    font-size: 104px;
    line-height: 1;
    letter-spacing: 6px;
    background: linear-gradient(180deg, var(--chrome-light) 0%, var(--chrome-mid) 48%, var(--chrome-dark) 52%, var(--chrome-light) 100%);
    -webkit-background-clip: text;
    background-clip: text;
    color: transparent;
    -webkit-text-stroke: 2px var(--outline);
  }
  .product-photo {
    position: absolute;
    left: 0;
    top: 748px;
    width: 100%;
    height: 221px;
    background: linear-gradient(135deg, var(--photo-light) 0%, var(--photo-mid) 50%, var(--photo-light) 100%);
  }
  .genuine-badge {
    position: absolute;
    left: 576px;
    top: 724px;
    width: 170px;
    height: 170px;
    border-radius: 50%;
    background: radial-gradient(circle at 40% 35%, var(--badge-red) 55%, var(--badge-dark) 100%);
    display: flex;
    flex-direction: column;
    align-items: center;
    justify-content: center;
    transform: rotate(-12deg);
    font-family: "Oswald", sans-serif;
    font-weight: 600;
    color: var(--badge-text);
    font-size: 34px;
    line-height: 1.05;
    text-align: center;
  }
  .quality-line {
    position: absolute;
    left: 0;
    top: 1000px;
    width: 100%;
    margin: 0;
    text-align: center;
    font-family: "Michroma", sans-serif;
    font-size: 42px;
    letter-spacing: 3px;
    background: linear-gradient(180deg, var(--chrome-light) 0%, var(--chrome-mid) 48%, var(--chrome-dark) 52%, var(--chrome-light) 100%);
    -webkit-background-clip: text;
    background-clip: text;
    color: transparent;
    -webkit-text-stroke: 1.5px var(--outline);
  }
</style>
</head>
<body>
<div class="canvas">
  <div class="poly-bag">
    <svg class="hang-hole" viewBox="0 0 100 46" aria-hidden="true">
      <path d="M20 14 H38 A12 12 0 0 1 62 14 H80 A16 16 0 0 1 80 46 H20 A16 16 0 0 1 20 14 Z" transform="translate(0,-2) scale(1,0.96)" fill="#ffffff" stroke="#222" stroke-width="2"/>
    </svg>

    <section class="brand-band">
      <span class="brand-mark-dot"></span>
      <h2 class="brand-name">VERONZO</h2>
    </section>

    <h1 class="product-title">CABLES</h1>

    <div class="product-photo" role="img" aria-label="Photo of black motorcycle control cables on crumpled white paper"></div>

    <div class="genuine-badge"><span>GENUINE</span><span>PARTS</span></div>

    <p class="quality-line">HIGH-QUALITY</p>
  </div>
</div>
</body>
</html>
```